Brambleton Law Stationary - Law Firm

I am looking for a designer who can help me design letterhead and envelopes consistent with our new business cards. Feel free to reach out to me directly at ned@brambletonlaw.example. Thank you!! Visit brambletonlaw.example to see our site and the attached files for creative assets.

Target Market(s)

Anyone needing a lawyer

Font styles to use
Other font styles liked:
• Adobe Caslon Pro

Requirements
Must have
• Adobe Caslon Pro font
Full color
Nice to have
• My photo on front along with 2/3 face of camo - see mock up for example of what I have in mind.

American colors - similar to the ones found on my website and gold.

```html
<!DOCTYPE html>
<html lang="en">
<head>
<meta charset="utf-8">
<title>Brambleton Law Stationery</title>
<link href="https://fonts.googleapis.com/css2?family=Libre+Caslon+Text:wght@400&family=Lato:wght@400;700&family=Roboto:wght@400&display=swap" rel="stylesheet">
<style>
  :root {
    --backdrop: #e4e4e4;
    --paper: #ffffff;
    --gold: #a8924f;
    --navy: #0e2746;
    --ink: #2b2b2b;
    --body-grey: #8c8c8c;
    --faint: #f1f2f3;
  }
  * { box-sizing: border-box; margin: 0; padding: 0; }
  html, body { width: 1200px; height: 900px; overflow: hidden; }
  body { background: var(--backdrop); position: relative; font-family: "Lato", sans-serif; }

  .sheet { position: absolute; background: var(--paper); overflow: hidden; }
  .letterhead { left: 62px; top: 126px; width: 514px; height: 665px; }
  .envelope-back { left: 606px; top: 262px; width: 541px; height: 248px; }
  .envelope-front { left: 606px; top: 541px; width: 541px; height: 248px; }

  .brand { position: absolute; display: flex; align-items: center; gap: 9px; }
  .brand-dot { width: 12px; height: 12px; border-radius: 50%; background: var(--gold); }
  .brand-name {
    font-family: "Libre Caslon Text", serif; font-weight: 400;
    color: var(--gold); font-size: 17px; letter-spacing: 1.2px; text-transform: uppercase;
  }
  .letterhead .brand { left: 42px; top: 54px; }
  .envelope-front .brand { left: 41px; top: 43px; }

  .contact-rule { position: absolute; left: 369px; top: 43px; width: 1px; height: 49px; background: var(--gold); }
  .contact { position: absolute; left: 383px; top: 44px; font-family: "Roboto", sans-serif; font-size: 7.6px; color: var(--ink); line-height: 10px; }
  .contact .address { margin-bottom: 5px; }
  .contact-line { display: flex; align-items: center; gap: 4px; height: 9.4px; }
  .contact-line svg { width: 6px; height: 6px; }

  .salutation { position: absolute; left: 49px; top: 182px; font-size: 11px; font-weight: 700; color: var(--ink); }
  .date { position: absolute; right: 46px; top: 181px; font-size: 11px; color: #6f6f6f; }
  .body-copy { position: absolute; left: 48px; width: 417px; font-size: 9px; line-height: 18.7px; color: var(--body-grey); text-align: justify; }
  .body-copy.first { top: 227px; }
  .body-copy.second { top: 340px; }
  .signature { position: absolute; left: 48px; top: 514px; width: 102px; height: 32px; background: linear-gradient(90deg, #ececec, #f6f6f6); border-radius: 4px; }

  .faint-mark { position: absolute; border-radius: 50%; background: var(--faint); }
  .letterhead .faint-mark { left: 380px; top: 460px; width: 124px; height: 124px; }
  .envelope-front .faint-mark { left: 414px; top: 58px; width: 124px; height: 124px; }

  .flap { position: absolute; left: 0; top: 0; }
  .flap-name {
    position: absolute; left: 0; width: 541px; top: 36px; text-align: center;
    font-family: "Libre Caslon Text", serif; font-size: 11px; letter-spacing: 1px;
    color: var(--gold); text-transform: uppercase;
  }

  .return-address { position: absolute; left: 41px; top: 82px; font-family: "Roboto", sans-serif; font-size: 7.3px; line-height: 9.8px; color: var(--ink); }
</style>
</head>
<body>

<section class="sheet letterhead">
  <div class="brand"><span class="brand-dot"></span><span class="brand-name">Brambleton Law</span></div>
  <div class="contact-rule"></div>
  <div class="contact">
    <div class="address">214 Linden Court<br>Marlow, Florida 32000</div>
    <div class="contact-line"><svg viewBox="0 0 10 10"><path d="M2 1l2 2-1 1.5c.8 1.5 1.5 2.2 3 3L7.5 6l2 2-1.5 1.5C4.5 9 1 5.5.5 2.5z" fill="#a8924f"/></svg>(555) 014-2290</div>
    <div class="contact-line"><svg viewBox="0 0 10 10"><rect x="0.5" y="2" width="9" height="6" fill="#a8924f"/><path d="M.5 2L5 5.5 9.5 2" stroke="#fff" fill="none"/></svg>ned@brambletonlaw.example</div>
    <div class="contact-line"><svg viewBox="0 0 10 10"><circle cx="5" cy="5" r="4.2" fill="none" stroke="#a8924f"/><path d="M1 5h8M5 1v8" stroke="#a8924f" stroke-width=".7"/></svg>www.brambletonlaw.example</div>
  </div>

  <p class="salutation">Dear Mr. Smith,</p>
  <p class="date">Oct. 20, 2021</p>

  <div class="faint-mark"></div>

  <p class="body-copy first">Lorem ipsum dolor sit amet, consectetur adipiscing elit, sed do eiusmod tempor incididunt ut labore et dolore magna aliqua. Ut enim ad minim veniam, quis nostrud exercitation ullamco laboris nisi ut aliquip ex ea commodo consequat. Duis aute irure dolor in reprehenderit in voluptate velit esse cillum dolore eu fugiat nulla pariatur. Excepteur sint occaecat cupidatat non proident, sunt in culpa qui officia deserunt mollit anim id est laborum.</p>
  <p class="body-copy second">Lorem ipsum dolor sit amet, consectetur adipiscing elit, sed do eiusmod tempor incididunt ut labore et dolore magna aliqua. Ut enim ad minim veniam, quis nostrud exercitation ullamco laboris nisi ut aliquip ex ea commodo consequat. Duis aute irure dolor in reprehenderit in voluptate velit esse cillum dolore eu fugiat nulla pariatur. Excepteur sint occaecat cupidatat non proident, sunt in culpa qui officia deserunt mollit anim id est laborum.Lorem ipsum dolor sit amet, consectetur adipiscing elit, sed do eiusmod tempor incididunt ut labore et dolore magna aliqua. Ut enim ad minim veniam, quis nostrud exercitation consectetur adipiscing elit, sed do eiusmod tempor incididunt ut labore et dolore magna aliqua. Ut enim ad minim veniam, quis nostrud exercitation.</p>

  <div class="signature" role="img" aria-label="Handwritten signature"></div>
</section>

<section class="sheet envelope-back">
  <svg class="flap" width="541" height="90" viewBox="0 0 541 90">
    <path d="M0 0H541L534 62Q530 86 505 86H36Q12 86 8 62Z" fill="#0e2746"/>
  </svg>
  <span class="flap-name">Brambleton Law</span>
</section>

<section class="sheet envelope-front">
  <div class="faint-mark"></div>
  <div class="brand"><span class="brand-dot"></span><span class="brand-name">Brambleton Law</span></div>
  <div class="return-address">214 Linden Court<br>Marlow, Florida 32000</div>
</section>

</body>
</html>
```